amber lanterns

We are in need of a website for married spouses or wives that are looking for a one night stand or affair, trying to get out from their marriage routine. We want our website for married people only.

i have extended my deadline until the 29 of april. we are looking for at least 8 pages if possible, but we would only like to see the first page as an example for the next few pages. if we really like your design we weill hire you and thenĀ  we talk about the rest of the pages and the money. if you have any comments or questions, don't be afraid to ask.

• We want to be able to have a link open to a future website. it needs pop ups and ads. we would like it to say at the bottom of the page, bolded and highlighted that, " We are not responsible for any sexually transmitted diseases" and " We are not responsible for any marriage break-ups or any problems in consequence after the encounters." " It is the responsibility of the subscriber(member) to have enough information about the person before the encounter." We would like the website to be compatible to fundora. The subscribers must be able to web chat, upload photos, and upload videos but can decide who can see them or watch them.They can also have the choice to block certain members from their profile.

```html
<!DOCTYPE html>
<html lang="en">
<head>
<meta charset="utf-8">
<title>Amber Lanterns – Home</title>
<link href="https://fonts.googleapis.com/css2?family=Arimo:wght@400;700&family=Delius+Swash+Caps&display=swap" rel="stylesheet">
<style>
:root{
  --page:#f3f4f7;
  --ink-blue:#1d5282;
  --brand-blue:#2a6fa8;
  --bar:#2b6593;
  --bar-dark:#1f4f77;
  --hero-band:#c9d2e0;
  --section:#a8b5cc;
  --panel:rgba(168,172,182,.78);
  --heading-script:#2e7dbd;
  --link:#1f5f99;
  --footer:#5e6167;
  --footer-text:#d6e5f6;
  --white:#ffffff;
  --card-frame:#e6e6e8;
  --thumb-frame:#2a2c30;
}
*{box-sizing:border-box;margin:0;padding:0}
html,body{width:1131px;height:1200px;overflow:hidden;background:var(--page)}
body{font-family:"Arimo",Arial,sans-serif;color:#222}
.canvas{position:relative;width:1131px;height:1200px;background:var(--page);overflow:hidden}
.abs{position:absolute}

/* header */
.brand-mark{left:105px;top:9px;width:66px;height:66px;background:var(--brand-blue);border-radius:4px}
.brand-name{left:60px;top:78px;width:160px;text-align:center;font-size:14px;color:var(--brand-blue);letter-spacing:.2px}
.user-menu{right:82px;top:32px;display:flex;gap:18px;font-size:14px;color:var(--ink-blue)}
.user-menu span.sep{color:var(--ink-blue)}

/* main navigation */
.main-nav{left:0;top:124px;width:1131px;height:28px;background:var(--bar)}
.nav-home{left:118px;top:127px;width:113px;height:22px;border-radius:11px;background:linear-gradient(#5fc4ef,#1f8fcf);color:#fff;font-size:13px;text-align:center;line-height:22px}
.nav-item{top:124px;line-height:28px;color:#fff;font-size:13px}

/* hero */
.hero-band{left:0;top:152px;width:1131px;height:213px;background:var(--hero-band)}
.hero-white{left:0;top:365px;width:1131px;height:82px;background:var(--white)}
.why-title{left:95px;top:172px;font-family:"Delius Swash Caps",cursive;font-size:27px;color:var(--heading-script)}
.points-photo{left:99px;top:216px;width:423px;height:219px;background:linear-gradient(180deg,#efe3da 0%,#f3d9c9 55%,#c9b7a6 100%);box-shadow:0 2px 6px rgba(0,0,0,.18)}
.points-list{left:125px;top:238px;list-style:none}
.points-list li{height:31px;display:flex;align-items:center;gap:8px;font-size:14px;color:#2a5f8f}

/* search panel */
.search-panel{left:607px;top:152px;width:423px;height:281px;background:var(--panel)}
.search-title{left:636px;top:166px;color:#3d86c6;font-size:18px}
.search-title b{font-weight:400;font-size:25px;color:#1f67ad}
.field-label{width:200px;left:559px;text-align:right;font-size:14px;color:#1f4a78}
.select{left:785px;width:178px;height:22px;background:#fff;border:1px solid #8a8d92;font-size:12px;color:#333;padding-left:6px;line-height:20px}
.select::after{content:"";position:absolute;right:0;top:0;width:18px;height:20px;background:#e3e3e3;border-left:1px solid #999}
.select i{position:absolute;right:5px;top:8px;z-index:1;border:4px solid transparent;border-top-color:#222}
.box-input{height:22px;background:#fff;border:1px solid #8a8d92;font-size:12px;line-height:20px;padding-left:6px;color:#333}
.search-btn{left:786px;top:391px;width:94px;height:29px;background:linear-gradient(#f7f7f7,#d7d7d7);border:1px solid #b5b5b5;font-size:14px;color:#1f4a78;text-align:center;line-height:27px}

/* section bars */
.section-bar{left:0;width:1131px;height:28px;background:var(--bar)}
.section-title{left:115px;line-height:28px;color:#fff;font-size:14px}
.section-bg{left:0;width:1131px;background:var(--section)}

/* videos */
.nav-arrow{width:50px;height:50px}
.video-thumb{top:496px;width:161px;height:126px;background:var(--thumb-frame);padding:4px}
.video-thumb .still{width:153px;height:100px;background:linear-gradient(135deg,#c9a88c,#6d7c6f 60%,#3a4b55)}
.video-thumb .controls{height:16px;margin-top:2px;background:#111;display:flex;align-items:center;gap:6px;padding:0 4px;font-size:7px;color:#ccc}
.video-thumb .track{flex:1;height:3px;background:#666;border-radius:2px}
.play{left:62px;top:42px;width:34px;height:22px;background:rgba(230,230,230,.85);border-radius:4px}
.video-name{font-size:16px;font-weight:700;color:#111}
.video-meta{font-size:13px;color:#333}

/* profile cards */
.card{top:762px;width:200px;height:204px;background:var(--card-frame);padding:9px}
.card .photo{width:182px;height:186px}
.card .caption{position:absolute;left:9px;bottom:11px;width:182px;height:49px;background:rgba(40,40,40,.7);color:#fff;text-align:center;font-size:14px;padding-top:7px;line-height:20px}
.pager{top:990px;display:flex;gap:0;font-size:14px;color:var(--link)}

/* footer */
.site-footer{left:0;top:1046px;width:1131px;height:154px;background:var(--footer)}
.disclaimer{left:130px;top:1063px;width:900px;font-size:12.3px;line-height:21px;color:var(--footer-text)}
.copyright{left:130px;top:1153px;font-size:12px;color:#fff}
.partners{right:106px;top:1135px;display:flex;gap:12px;font-size:13px;color:#fff}
.partners span{display:flex;align-items:center;gap:5px}
.partners span::before{content:"";width:12px;height:12px;background:#e8eef6;border-radius:2px}
</style>
</head>
<body>
<div class="canvas">

  <header>
    <div class="abs brand-mark"></div>
    <div class="abs brand-name">AMBER LANTERNS</div>
    <nav class="abs user-menu">
      <span>Welcome User</span><span class="sep">|</span>
      <span>Logout</span><span class="sep">|</span>
      <span>My Profile</span><span class="sep">|</span>
      <span>Settings</span>
    </nav>
  </header>

  <nav>
    <div class="abs main-nav"></div>
    <div class="abs nav-home">HOME</div>
    <div class="abs nav-item" style="left:308px">FIND OUR PARTNER</div>
    <div class="abs nav-item" style="left:522px">JOIN NOW</div>
    <div class="abs nav-item" style="left:711px">MEMBER LOGIN</div>
  </nav>

  <section class="hero">
    <div class="abs hero-band"></div>
    <div class="abs hero-white"></div>
    <h1 class="abs why-title" style="font-weight:400">Why Join Amber Lanterns?</h1>
    <div class="abs points-photo" role="img" aria-label="Woman sitting on a rock looking out at a calm pastel sea"></div>
    <ul class="abs points-list">
      <li><svg width="11" height="16" viewBox="0 0 11 16"><path d="M2 1l7 7-7 7" fill="none" stroke="#2e86c8" stroke-width="3"/></svg>Lorem Ipsum POINT 1</li>
      <li><svg width="11" height="16" viewBox="0 0 11 16"><path d="M2 1l7 7-7 7" fill="none" stroke="#2e86c8" stroke-width="3"/></svg>Lorem Ipsum POINT 1</li>
      <li><svg width="11" height="16" viewBox="0 0 11 16"><path d="M2 1l7 7-7 7" fill="none" stroke="#2e86c8" stroke-width="3"/></svg>Lorem Ipsum POINT 1</li>
      <li><svg width="11" height="16" viewBox="0 0 11 16"><path d="M2 1l7 7-7 7" fill="none" stroke="#2e86c8" stroke-width="3"/></svg>Lorem Ipsum POINT 1</li>
      <li><svg width="11" height="16" viewBox="0 0 11 16"><path d="M2 1l7 7-7 7" fill="none" stroke="#2e86c8" stroke-width="3"/></svg>Lorem Ipsum POINT 1</li>
      <li><svg width="11" height="16" viewBox="0 0 11 16"><path d="M2 1l7 7-7 7" fill="none" stroke="#2e86c8" stroke-width="3"/></svg>Lorem Ipsum POINT 1</li>
    </ul>

    <div class="abs search-panel"></div>
    <div class="abs search-title">Searching for <b>SEX DATING</b></div>
    <div class="abs field-label" style="top:200px">I am / We are a</div>
    <div class="abs select" style="top:198px">woman<i></i></div>
    <div class="abs field-label" style="top:232px">Seeking a</div>
    <div class="abs select" style="top:229px">Man<i></i></div>
    <div class="abs field-label" style="top:266px">Between the ages of</div>
    <div class="abs box-input" style="left:785px;top:260px;width:39px">18</div>
    <div class="abs" style="left:832px;top:264px;font-size:14px;color:#1f4a78">and</div>
    <div class="abs box-input" style="left:865px;top:260px;width:38px">35</div>
    <div class="abs field-label" style="top:299px">Country</div>
    <div class="abs select" style="top:294px">Isreal<i></i></div>
    <div class="abs field-label" style="top:332px">State / Provience</div>
    <div class="abs select" style="top:327px">Any<i></i></div>
    <div class="abs field-label" style="top:365px">Zip Code (U.S. only)</div>
    <div class="abs box-input" style="left:785px;top:360px;width:60px"></div>
    <div class="abs search-btn">Search</div>
  </section>

  <section class="member-videos">
    <div class="abs section-bar" style="top:450px"></div>
    <svg class="abs" style="left:86px;top:453px" width="22" height="22" viewBox="0 0 22 22"><path d="M11 1l10 10-10 10L1 11z" fill="#1a1a1a"/><path d="M11 5l6 6-6 6-6-6z" fill="#9bb8d6"/></svg>
    <div class="abs section-title" style="top:450px">MEMBER VIDEOS</div>
    <div class="abs section-bg" style="top:478px;height:226px"></div>

    <svg class="abs nav-arrow" style="left:83px;top:540px" viewBox="0 0 50 50"><circle cx="25" cy="25" r="23" fill="#e9f3fb" stroke="#2f7fc2" stroke-width="3"/><circle cx="25" cy="25" r="17" fill="#3f96d6"/><path d="M28 16l-9 9 9 9" fill="none" stroke="#fff" stroke-width="4"/></svg>
    <svg class="abs nav-arrow" style="left:999px;top:540px" viewBox="0 0 50 50"><circle cx="25" cy="25" r="23" fill="#e9f3fb" stroke="#2f7fc2" stroke-width="3"/><circle cx="25" cy="25" r="17" fill="#3f96d6"/><path d="M22 16l9 9-9 9" fill="none" stroke="#fff" stroke-width="4"/></svg>

    <div class="abs video-thumb" style="left:162px"><div class="still" role="img" aria-label="Video still of a blonde member"></div><div class="controls"><span>▶</span><div class="track"></div><span>0:00 / 5:23</span></div><div class="abs play"></div></div>
    <div class="abs video-thumb" style="left:376px"><div class="still" role="img" aria-label="Video still of a member by a waterfront"></div><div class="controls"><span>▶</span><div class="track"></div><span>0:00 / 5:23</span></div><div class="abs play"></div></div>
    <div class="abs video-thumb" style="left:592px"><div class="still" role="img" aria-label="Video still of a blonde member"></div><div class="controls"><span>▶</span><div class="track"></div><span>0:00 / 5:23</span></div><div class="abs play"></div></div>
    <div class="abs video-thumb" style="left:804px"><div class="still" role="img" aria-label="Video still of a member by a waterfront"></div><div class="controls"><span>▶</span><div class="track"></div><span>0:00 / 5:23</span></div><div class="abs play"></div></div>

    <div class="abs" style="left:162px;top:627px"><div class="video-name">agirlwatcher 29/f</div><div class="video-meta" style="margin-top:6px">Madras</div><div class="video-meta" style="margin-top:7px">Looking for Hookups</div></div>
    <div class="abs" style="left:376px;top:627px"><div class="video-name">agirlwatcher 29/f</div><div class="video-meta" style="margin-top:6px">Madras</div><div class="video-meta" style="margin-top:7px">Looking for Hookups</div></div>
    <div class="abs" style="left:592px;top:627px"><div class="video-name">agirlwatcher 29/f</div><div class="video-meta" style="margin-top:6px">Madras</div><div class="video-meta" style="margin-top:7px">Looking for Hookups</div></div>
    <div class="abs" style="left:804px;top:627px"><div class="video-name">agirlwatcher 29/f</div><div class="video-meta" style="margin-top:6px">Madras</div><div class="video-meta" style="margin-top:7px">Looking for Hookups</div></div>
  </section>

  <section class="latest-girls">
    <div class="abs section-bar" style="top:725px"></div>
    <svg class="abs" style="left:86px;top:728px" width="22" height="22" viewBox="0 0 22 22"><path d="M11 1L21 20H1z" fill="#3a9be0"/><path d="M11 8L17 20H5z" fill="#8fd0f7"/></svg>
    <div class="abs section-title" style="top:725px">LATEST GIRLS</div>
    <div class="abs section-bg" style="top:753px;height:272px"></div>

    <div class="abs card" style="left:129px"><div class="photo" role="img" aria-label="Profile photo of Brany" style="background:linear-gradient(160deg,#d8c8b8,#b48d7a 55%,#c23f7f)"></div><div class="caption">BRANY<br>Age-23,Russian</div></div>
    <div class="abs card" style="left:367px"><div class="photo" role="img" aria-label="Profile photo of Marian" style="background:linear-gradient(160deg,#4a3d38,#8c6a5a 55%,#2f3c4a)"></div><div class="caption">MARIAN<br>Age-24,Mexican</div></div>
    <div class="abs card" style="left:598px"><div class="photo" role="img" aria-label="Profile photo of Suzan" style="background:linear-gradient(160deg,#f3b6c8,#d9a289 55%,#efe2dc)"></div><div class="caption">SUZAN<br>Age-26,Canada</div></div>
    <div class="abs card" style="left:834px"><div class="photo" role="img" aria-label="Profile photo of Mona" style="background:linear-gradient(160deg,#3e4145,#8d6e60 55%,#2a2b2e)"></div><div class="caption">MONA<br>Age-27,Turkey</div></div>

    <nav class="abs pager" style="left:803px">Previous</nav>
    <nav class="abs pager" style="left:876px">1</nav>
    <nav class="abs pager" style="left:908px">2</nav>
    <nav class="abs pager" style="left:939px">3</nav>
    <nav class="abs pager" style="left:971px">4</nav>
    <nav class="abs pager" style="left:1003px">Next</nav>
  </section>

  <footer>
    <div class="abs site-footer"></div>
    <p class="abs disclaimer">"We are not responsible for any sexually transmitted diseases" and "We are not responsible for any marriage break-ups or any problems in &nbsp;consequence after the encounters"."It is the responsibility of the subscriber (member) to have enough information about the person before the encounter".</p>
    <div class="abs copyright">copyrights@2012.All Rights Reserved</div>
    <div class="abs partners"><span>fundora</span><span>skylark</span><span>friendloop</span></div>
  </footer>

</div>
</body>
</html>
```